Business Card and Envelope Layout Change/Font Increase

Very simple job, sorry. I need the address on my envelope moved from the lower left corner and placed under my logo in the upper left corner and the overall font size of the address increased to about twice of what it is so it is easier to read. Also, on the envelope, my website and email address can remain in the lower right corner but I would like the font size also increased.
As for the business card, I would like the vertical "I speak Spanish/Yo hablo Espanol" removed. I would also like the font size of the text in the blue area slightly increased for easier reading. Final change are the credentials under the name. Please delete what is currently there (LMHC, NCC, DCC) and add the following: PhD., LMHC, CMHS, ACS.
I am attaching the eps files for the envelope and the photoshop file for the business card.
As described in the description, just some minor changes. I already have the files for the back of the business card as there are no changes for that.

```html
<!DOCTYPE html>
<html lang="en">
<head>
<meta charset="utf-8">
<title>Birch Counseling Envelope</title>
<link rel="stylesheet" href="https://fonts.googleapis.com/css2?family=Questrial&family=Cinzel:wght@600&display=swap">
<style>
  :root {
    --brand-blue: #2c5f96;
    --brand-green: #467337;
    --paper: #ffffff;
    --text-blue: #2c5f96;
    --text-green: #467337;
  }
  html, body {
    margin: 0;
    padding: 0;
    width: 1200px;
    height: 570px;
    overflow: hidden;
    background: var(--paper);
  }
  .envelope {
    position: relative;
    width: 1200px;
    height: 570px;
    background: var(--paper);
    overflow: hidden;
    font-family: "Questrial", "Century Gothic", sans-serif;
  }
  .band {
    position: absolute;
    left: 0;
    width: 1200px;
    height: 63px;
    display: block;
  }
  .band--top { top: 0; }
  .band--bottom { bottom: 0; }
  .band__blue { fill: var(--brand-blue); }
  .band__green { fill: var(--brand-green); }

  .sender {
    position: absolute;
    left: 79px;
    top: 96px;
  }
  .brand {
    display: flex;
    align-items: center;
    gap: 10px;
    height: 68px;
  }
  .brand__dot {
    width: 56px;
    height: 56px;
    border-radius: 50%;
    background: var(--brand-green);
    flex: none;
  }
  .brand__name {
    font-family: "Cinzel", serif;
    font-weight: 600;
    font-size: 24px;
    line-height: 1.05;
    color: var(--text-blue);
    letter-spacing: 0.5px;
  }
  .sender__address {
    margin-top: 17px;
    font-style: normal;
    font-size: 16.5px;
    line-height: 21.5px;
    color: var(--text-blue);
  }
  .sender__phone {
    font-size: 15px;
  }
  .web-contact {
    position: absolute;
    right: 91px;
    top: 446px;
    text-align: right;
    color: var(--text-green);
    font-size: 15.5px;
    line-height: 26px;
    letter-spacing: 3.2px;
  }
  .web-contact__line { display: block; }
  .web-contact__line--site { margin-right: 11px; }
</style>
</head>
<body>
  <div class="envelope">
    <svg class="band band--top" viewBox="0 0 1200 63" aria-hidden="true">
      <polygon class="band__blue" points="0,0 798,0 739,63 0,63"/>
      <polygon class="band__green" points="832,0 1200,0 1200,63 772,63"/>
    </svg>

    <div class="sender">
      <div class="brand">
        <span class="brand__dot" aria-hidden="true"></span>
        <span class="brand__name">Birch<br>Counseling</span>
      </div>
      <address class="sender__address">
        4180 Alder Grove Rd, Suite B2<br>
        Fernhill, WA 98512<br>
        <span class="sender__phone">Tel: 360 / 555 - 0148</span>
      </address>
    </div>

    <div class="web-contact">
      <span class="web-contact__line">markt@birchcounselingllc.com</span>
      <span class="web-contact__line web-contact__line--site">www.birchcounselingllc.com</span>
    </div>

    <svg class="band band--bottom" viewBox="0 0 1200 63" aria-hidden="true">
      <polygon class="band__blue" points="0,0 754,0 694,63 0,63"/>
      <polygon class="band__green" points="790,0 1200,0 1200,63 728,63"/>
    </svg>
  </div>
</body>
</html>
```